Diesel Fitting/Mechanical Company Needs a new Business Card

We would like a new business card that showcases our logo and business information.

Industry/Entity Type

Business

Contact Information for Business Card

314 Wendale Street
PO Box 7581 BRAMLEY FLATS QLD 4827
Phone: 49312787 Fax: 49312688 Mobile: 0438915276 ABN: 63 519 087 342

Requirements
Must have
• The following email addresses:
• admin@tkservicing.com.au , sales@tkservicing.com.au , accounts@tkservicing.com.au , parts@tkservicing.com.au , office@tkservicing.com.au
• Also need to have the website: www.tkservicing.com.au

```html
<!DOCTYPE html>
<html lang="en">
<head>
<meta charset="utf-8">
<title>TK Servicing – Business Card</title>
<link href="https://fonts.googleapis.com/css2?family=Questrial&family=Tinos:wght@700&family=Open+Sans:wght@400&display=swap" rel="stylesheet">
<style>
  :root{
    --stage:#3a3a3c;
    --stage-top:#ffffff;
    --card-front:#ffffff;
    --card-back:#9b9b9b;
    --ink:#111111;
    --muted:#9a9a9a;
    --icon:#8d8d8d;
    --accent:#f07f22;
    --back-ink:#ffffff;
  }
  *{margin:0;padding:0;box-sizing:border-box}
  html,body{width:1200px;height:935px;overflow:hidden}
  body{background:var(--stage);position:relative;font-family:"Questrial",sans-serif;color:var(--ink)}
  .top-edge{position:absolute;left:0;top:0;width:1200px;height:8px;background:var(--stage-top)}
  .card{position:absolute;left:253px;width:652px;height:372px;border-radius:16px;box-shadow:8px 10px 14px rgba(0,0,0,.45)}
  .card--front{top:40px;background:var(--card-front)}
  .card--back{top:499px;background:var(--card-back)}
  .holder-name{position:absolute;left:33px;top:48px;font-family:"Tinos",serif;font-weight:700;font-size:28px;line-height:1}
  .holder-role{position:absolute;left:33px;top:79px;font-size:19px;line-height:1}
  .address{position:absolute;left:33px;top:150px;font-size:19px;line-height:21.7px;font-style:normal}
  .contacts{position:absolute;left:33px;top:237px;list-style:none;font-size:19px;line-height:21.8px}
  .contacts li{display:flex;align-items:center}
  .contacts svg{width:12px;height:12px;margin-right:11px;fill:var(--icon)}
  .muted{color:var(--muted)}
  .emails{position:absolute;left:381px;top:212px;font-size:19px;line-height:21.8px;list-style:none}
  .email-icon{position:absolute;left:-26px;top:6px;width:12px;height:10px}
  .brand{position:absolute;color:var(--accent);font-size:22px;white-space:nowrap;display:flex;align-items:center}
  .brand .dot{display:inline-block;border-radius:50%;background:var(--accent);margin-right:8px}
  .brand--front{left:448px;top:88px}
  .brand--front .dot{width:14px;height:14px}
  .brand--back{left:50%;top:170px;transform:translateX(-50%);font-size:32px}
  .brand--back .dot{width:20px;height:20px;margin-right:10px}
  .abn{position:absolute;left:245px;top:335px;display:flex;align-items:center;font-family:"Open Sans",sans-serif;font-size:16px;color:var(--back-ink)}
  .abn .abn-icon{width:13px;height:13px;border-radius:50%;background:var(--accent);margin-right:10px}
</style>
</head>
<body>
  <div class="top-edge"></div>

  <section class="card card--front">
    <h1 class="holder-name">Martin Callow</h1>
    <p class="holder-role">Dirctor</p>

    <address class="address">
      314 Wendale Street<br>
      PO Box 7581<br>
      BRAMLEY FLATS QLD 4827
    </address>

    <ul class="contacts">
      <li><svg viewBox="0 0 12 12"><path d="M3 0h6v12H3zM4 1v9h4V1z"/></svg>49312787</li>
      <li><svg viewBox="0 0 12 12"><path d="M3 0h6v3H3zM0 4h12v5H10v3H2V9H0zM3 8v3h6V8z"/></svg>49312688</li>
      <li><svg viewBox="0 0 12 12"><path d="M2 0l3 3-1.5 1.5c1 2 2 3 4 4L9 7l3 3-2 2C5 11 1 7 0 2z"/></svg>0438915276</li>
      <li><svg viewBox="0 0 12 12"><path d="M6 0a6 6 0 1 0 0 12A6 6 0 0 0 6 0zm0 1c.8 0 1.6 1.8 1.8 4.5H4.2C4.4 2.8 5.2 1 6 1zM1 6.5h2.2c.1 1.6.4 3 .9 4A5 5 0 0 1 1 6.5zm0-1a5 5 0 0 1 3.1-4c-.5 1-.8 2.4-.9 4zm3.2 1h3.6C7.6 9.2 6.8 11 6 11s-1.6-1.800-1.8-4.5zm4.6 0H11a5 5 0 0 1-3.1 4c.5-1 .8-2.4.9-4zm0-1c-.1-1.6-.4-3-.9-4A5 5 0 0 1 11 5.5z"/></svg>www.<span class="muted">tkservicing</span>.com.au</li>
    </ul>

    <div class="brand brand--front"><span class="dot"></span>TK Servicing</div>

    <ul class="emails">
      <svg class="email-icon" viewBox="0 0 12 10" fill="none" stroke="#8d8d8d" stroke-width="1.2"><rect x=".6" y=".6" width="10.8" height="8.8"/><path d="M.6.6 6 5.5 11.4.6"/></svg>
      <li>admin@<span class="muted">tkservicing</span>.com.au</li>
      <li>sales@<span class="muted">tkservicing</span>.com.au</li>
      <li>accounts@<span class="muted">tkservicing</span>.com.au</li>
      <li>parts@<span class="muted">tkservicing</span>.com.au</li>
      <li>office@<span class="muted">tkservicing</span>.com.au</li>
    </ul>
  </section>

  <section class="card card--back">
    <div class="brand brand--back"><span class="dot"></span>TK Servicing</div>
    <p class="abn"><span class="abn-icon"></span>63 519 087 342</p>
  </section>
</body>
</html>
```